Electrical company needs a business card design that POPS!

We need a business card design for an Electrical Company - Bright Arc Electrical Designs. We would like one that is modern, sleek and professional while also being creative, innovative, and stands out from the rest! We are open to any ideas you might have. It needs to be in line with our company themed colours, which you will find on the attachment logos, also on our website. You are welcome to mix things up as much as you like in regards to the layout of our logo and the overall card design. You can take ideas from our website or implement your own ideas.
The business card needs the following info on it -

Garth Molloway
Director
REC 58317
PO Box 471
Kestrel Vale VIC 3999
M +64 (0)487 512 094
P 1300 682 915
E info@brightarcelectrical.example.com.au
W www.brightarcelectrical.example.com.au
Domestic - Commercial - Industrial - Maintenance
Lighting & Power
Data & Communications
Security, Alarm, CCTV
Heating & Cooling
Home Automation
Property Maintenance
New Installations, Refurbishments, upgrades

Once the business card is established we will be looking at getting a magnet design and flyers with the winning designer.

Target Market(s)

residential home owners, business owners, corporate companies, general public or anyone who could need an electrician

Industry/Entity Type

Electrician

Contact Information for Business Card

Garth Molloway
Director
REC 58317
PO Box 471
Kestrel Vale VIC 3999
M +64 (0)487 512 094
P 1300 682 915
Lighting & Power
Data & Communications
Security, Alarm, CCTV
Heating & Cooling
Home Automation
Property Maintenance

Requirements
Must have
• Must have Logo including the company name - Bright Arc Electrical. must have all of the info as listed in product description.
• Font for Bright Arc Electrical should be as per the image attached. open to other font ideas for all other info.
Nice to have
• we would like it to look very professional, sleek and not over-crowded. However still creative and have a designer edge to it. We want it to stand out and pop!

```html
<!DOCTYPE html>
<html lang="en">
<head>
<meta charset="utf-8">
<title>Bright Arc Electrical Designs – Business Card</title>
<link rel="stylesheet" href="https://fonts.googleapis.com/css2?family=Montserrat:wght@700&family=Open+Sans:wght@400;600&family=Noto+Serif&display=swap">
<style>
  :root {
    --ink: #111111;
    --band-black: #141414;
    --accent-red: #e02424;
    --paper: #ffffff;
    --card-edge: #d6d6d6;
  }
  * { box-sizing: border-box; margin: 0; padding: 0; }
  html, body { width: 851px; height: 1200px; overflow: hidden; background: var(--paper); }
  body { position: relative; font-family: "Open Sans", Arial, sans-serif; color: var(--ink); }

  .side-label {
    position: absolute; left: 0; width: 851px; text-align: center;
    font-family: "Noto Serif", Georgia, serif; font-size: 26px; color: #222;
  }
  .side-label--front { top: 22px; }
  .side-label--back { top: 640px; }

  .card {
    position: absolute; left: 51px; width: 770px; height: 456px;
    background: var(--paper); border: 1px solid var(--card-edge);
    box-shadow: 0 1px 4px rgba(0,0,0,0.15); overflow: hidden;
  }
  .card--front { top: 94px; }
  .card--back { top: 712px; }
  .card__band { position: absolute; inset: 0; width: 100%; height: 100%; }

  .holder { position: absolute; left: 204px; top: 52px; font-family: "Montserrat", Arial, sans-serif; font-weight: 700; font-size: 29px; line-height: 1.22; }

  .brand { position: absolute; right: 38px; top: 46px; display: flex; align-items: center; gap: 12px; }
  .brand__dot { width: 22px; height: 22px; border-radius: 50%; background: var(--accent-red); flex: none; }
  .brand__name { font-family: "Open Sans", Arial, sans-serif; font-weight: 600; font-size: 17px; line-height: 1.2; color: var(--accent-red); width: 150px; }

  .contacts { position: absolute; top: 300px; font-size: 15px; line-height: 21px; }
  .contacts--address { left: 204px; }
  .contacts--lines { left: 405px; }
  .contact-row { display: flex; }
  .contact-row__key { width: 24px; color: var(--accent-red); font-weight: 600; }

  .services { position: absolute; left: 268px; top: 106px; list-style: none; font-size: 16px; line-height: 28px; }
  .services li { position: relative; padding-left: 22px; }
  .services li::before {
    content: ""; position: absolute; left: 0; top: 11px; width: 7px; height: 7px;
    border-radius: 50%; background: var(--accent-red);
  }
</style>
</head>
<body>
  <div class="side-label side-label--front">Front</div>

  <section class="card card--front">
    <svg class="card__band" viewBox="0 0 770 456" aria-hidden="true">
      <polygon points="0,0 120,0 40,456 0,456" fill="var(--band-black)"/>
      <line x1="134" y1="0" x2="54" y2="456" stroke="var(--accent-red)" stroke-width="6"/>
    </svg>

    <div class="holder">Garth Molloway<br>Director</div>

    <div class="brand">
      <span class="brand__dot"></span>
      <span class="brand__name">Bright Arc Electrical Designs</span>
    </div>

    <div class="contacts contacts--address">
      <div class="contact-row"><span class="contact-row__key">A</span><span>REC 58317<br>PO Box 471<br>Kestrel Vale VIC 3999</span></div>
    </div>

    <div class="contacts contacts--lines">
      <div class="contact-row"><span class="contact-row__key">M</span><span>+64 (0)487 512 094</span></div>
      <div class="contact-row"><span class="contact-row__key">P</span><span>1300 682 915</span></div>
      <div class="contact-row"><span class="contact-row__key">E</span><span>info@brightarcelectrical.example.com.au</span></div>
      <div class="contact-row"><span class="contact-row__key">W</span><span>www.brightarcelectrical.example.com.au</span></div>
    </div>
  </section>

  <div class="side-label side-label--back">Back</div>

  <section class="card card--back">
    <svg class="card__band" viewBox="0 0 770 456" aria-hidden="true">
      <polygon points="0,0 120,0 40,456 0,456" fill="var(--band-black)"/>
      <line x1="134" y1="0" x2="54" y2="456" stroke="var(--accent-red)" stroke-width="6"/>
    </svg>

    <ul class="services">
      <li>Domestic - Commercial - Industrial - Maintenance</li>
      <li>Lighting &amp; Power</li>
      <li>Data &amp; Communications</li>
      <li>Security, Alarm, CCTV</li>
      <li>Heating &amp; Cooling</li>
      <li>Home Automation</li>
      <li>Property Maintenance</li>
      <li>New Installations, Refurbishments, Upgrades</li>
    </ul>
  </section>
</body>
</html>
```